Brevanta needs a business Card Design

We are looking for a business card Design for our new Managed Service Provider Company, Brevanta. Brevanta encompasses everything IT for the average medium sized business. Our primary services are help desk support, cyber-security (malware and ransomware protection), and Disaster Recovery systems. We would like the design to have a very clean and professional look, with a very minimalist feel.

Target Market(s)

Medium to large sized businesses

Industry/Entity Type

It Service

Contact Information for Business Card

Name GoesHere
name@brevanta-mail.net
O: 555-382-6047
C: 555-000-0000

Font styles to use
Other font styles liked:
• Poppins Font Only Please

Colors

Designer to choose only greyscale colors for use in the design.

Requirements
Must have
• Logo included
Nice to have
• Cutting Edge, innovative, minimalistic, elegant

```html
<!DOCTYPE html>
<html lang="en">
<head>
<meta charset="utf-8">
<title>Brevanta Business Card</title>
<link rel="stylesheet" href="https://fonts.googleapis.com/css2?family=Poppins:wght@300;400;500&display=swap">
<style>
  :root {
    --canvas-bg: #e4e4e4;
    --charcoal: #1c1c1c;
    --paper: #fbfbfb;
    --ink: #222222;
    --slate: #444444;
    --white: #ffffff;
    --url-grey: #d6d6d6;
    --shadow: rgba(0, 0, 0, 0.18);
  }
  * { box-sizing: border-box; margin: 0; padding: 0; }
  html, body {
    width: 1200px;
    height: 1020px;
    overflow: hidden;
    background: var(--canvas-bg);
    font-family: "Poppins", sans-serif;
  }
  .sheet {
    position: relative;
    width: 1200px;
    height: 1020px;
    display: flex;
    align-items: center;
    justify-content: center;
    gap: 40px;
  }
  .card {
    position: relative;
    width: 520px;
    height: 300px;
    box-shadow: 0 10px 28px var(--shadow);
  }

  /* Front */
  .card-front {
    background: var(--charcoal);
    color: var(--white);
    display: flex;
    flex-direction: column;
    align-items: center;
    justify-content: center;
  }
  .front-brand {
    display: flex;
    align-items: center;
    gap: 14px;
  }
  .front-brand .brand-square {
    width: 14px;
    height: 14px;
    background: var(--white);
  }
  .front-brand .brand-name {
    font-weight: 300;
    font-size: 38px;
    letter-spacing: 10px;
    text-transform: uppercase;
  }
  .front-url {
    margin-top: 22px;
    font-weight: 300;
    font-size: 12px;
    letter-spacing: 3px;
    color: var(--url-grey);
  }

  /* Back */
  .card-back {
    background: var(--paper);
    color: var(--ink);
  }
  .back-brand {
    position: absolute;
    left: 56px;
    top: 136px;
    font-weight: 400;
    font-size: 22px;
    letter-spacing: 3px;
    color: var(--slate);
  }
  .contact {
    position: absolute;
    left: 250px;
    top: 72px;
  }
  .contact-name {
    font-weight: 400;
    font-size: 24px;
    line-height: 1.1;
    letter-spacing: 0.5px;
    white-space: nowrap;
  }
  .contact-title {
    font-weight: 400;
    font-size: 11px;
    letter-spacing: 0.5px;
    margin-top: 2px;
    margin-bottom: 14px;
  }
  .contact-list { list-style: none; }
  .contact-list li {
    display: flex;
    align-items: center;
    gap: 8px;
    font-size: 12px;
    line-height: 22px;
    white-space: nowrap;
  }
  .contact-list svg {
    width: 12px;
    height: 12px;
    fill: var(--ink);
    flex: none;
  }
</style>
</head>
<body>
<main class="sheet">
  <section class="card card-front">
    <div class="front-brand">
      <span class="brand-square"></span>
      <span class="brand-name">Brevanta</span>
    </div>
    <p class="front-url">www.brevanta-mail.net</p>
  </section>

  <section class="card card-back">
    <p class="back-brand">Brevanta</p>
    <div class="contact">
      <h1 class="contact-name">Name GoesHere</h1>
      <p class="contact-title">JOB TITLE</p>
      <ul class="contact-list">
        <li>
          <svg viewBox="0 0 12 12" aria-hidden="true"><path d="M1 4c0-1.5 2-2.5 5-2.5S11 2.5 11 4v1H8.5V4h-5v1H1zM3 6h6l1.5 4.5h-9z"/></svg>
          555-382-6047
        </li>
        <li>
          <svg viewBox="0 0 12 12" aria-hidden="true"><path d="M3.5 0.5h5a1 1 0 0 1 1 1v9a1 1 0 0 1-1 1h-5a1 1 0 0 1-1-1v-9a1 1 0 0 1 1-1zM4 2v7h4V2zM5.5 9.6h1v0.8h-1z"/></svg>
          555-000-0000
        </li>
        <li>
          <svg viewBox="0 0 12 12" aria-hidden="true"><path d="M0.5 2.5h11v7h-11zM1.5 3.5v0.4L6 7l4.5-3.1v-0.4zM1.5 5.1v3.4h9V5.1L6 8.2z"/></svg>
          name@brevanta-mail.net
        </li>
      </ul>
    </div>
  </section>
</main>
</body>
</html>
```